Voice agent website redesign, responsive. Current website functional, needs fresh look.

** updated 01/04/2015 ** Stock photos and video OK
TQ Sounds is redesigning their website to refresh the look and feel and also to make the website more useable in portable devices.
We also intend to replace our existing iPhone app with responsive HTML.
We want to keep the features but update the way they are displayed.
The current website is at: http://www.tqsounds-demo.com.au. (examples of important pages are in the attachments)
The current website is written in .NET and MS SQL but designs optimised for WordPress will also be accepted.
We have corporate colours and a logo
We want a dynamic element on the front page
We do not mind the idea of a slider, but I must be modern and capable of video backgrounds
We like the clean design of our main competitor: http://www.zelvar-demo.com.au but the site is busy and not responsive.
The site must be designed to use responsive HTML and be easy to see and navigate using smaller viewports.
Once awarded the contract the designer must supply 4 pages in 3 formats, for which we will pay an extra $80, as outlined below:
Submission for selection
Designs must be submitted for selection with 1 required page (home page) in 1 required resolution and 1 optional resolution;
Versions:
• (Required) Full page web landscape – 1920 x 1080
• (Optional) Low resolution portrait (e.g. iPhone 3/4) – 320 x 480
Submission required when awarded
Final supplied designs must have 3 versions of 4 required pages as layered Photoshop files;
Versions:
• Full page web landscape – 1920 x 1080
• Medium resolution landscape (e.g. iPad) – 1024 x 768
• Low resolution portrait (e.g. iPhone 3/4) – 320 x 480
Pages:
• home page
• generic template
• search results
• talent page
The designer may also offer to convert the site into HTML and CSS for an added fee.
The attachments supplied contains important features like site menu and required elements, but only guidelines to design.
Please do read carefully for details on required elements, but do feel free to change the design, look and feel completely.
Attached are;
Target Market(s)
Advertising agencies who hire voice artists, also a showcase for the artists themselves
Look and feel

```html
<!DOCTYPE html>
<html lang="en">
<head>
<meta charset="utf-8">
<title>TQ Sounds</title>
<link rel="stylesheet" href="https://fonts.googleapis.com/css2?family=Roboto:wght@400;500;700&display=swap">
<style>
:root{
  --navy:#0b3d66;
  --panel-blue:#33648a;
  --green:#8cc63f;
  --green-dark:#5d9a2a;
  --band:#ececec;
  --card:#f4f4f4;
  --text:#333;
  --white:#fff;
}
*{box-sizing:border-box;margin:0;padding:0}
html,body{width:990px;height:1200px;overflow:hidden}
body{font-family:"Roboto",Arial,sans-serif;color:var(--text);background:var(--white);position:relative}
.abs{position:absolute}

.site-header{left:0;top:0;width:990px;height:126px;background:var(--navy)}
.brand{left:116px;top:22px;display:flex;align-items:center;gap:10px;color:var(--white);font-size:30px;font-weight:700;letter-spacing:-.5px}
.brand-mark{width:22px;height:40px;background:var(--green)}
.phones{right:118px;top:14px;color:var(--white);font-size:16px;line-height:25px;font-weight:500;text-align:right;white-space:nowrap}
.main-nav{left:116px;top:88px;width:756px;height:38px;background:var(--green);display:flex}
.main-nav a{color:var(--white);text-decoration:none;font-size:15px;line-height:38px;padding:0 13px}
.main-nav a.active{background:var(--white);color:#222;width:81px;text-align:center;padding:0}

.feature-band{left:0;top:126px;width:990px;height:400px;background:var(--band)}
.video{left:22px;top:139px;width:630px;height:370px;background:#111;overflow:hidden}
.video-frame{left:0;top:0;width:630px;height:336px;background:linear-gradient(100deg,#3b3a44 0%,#8a6c55 35%,#b9a28a 55%,#5a4a48 80%,#2d2b30 100%)}
.video-title{left:0;top:0;width:630px;height:28px;background:rgba(0,0,0,.55);color:#fff;font-size:14px;line-height:28px;padding-left:26px}
.play{left:276px;top:141px;width:78px;height:54px;border-radius:12px;background:rgba(20,20,20,.85)}
.controls{left:0;top:336px;width:630px;height:34px;background:#1b1b1b;color:#ddd;font-size:11px}
.progress{left:0;top:338px;width:630px;height:4px;background:#555}

.recent{left:685px;top:139px;width:289px;height:375px;background:var(--card)}
.recent h2{position:absolute;left:14px;top:12px;font-size:18px;font-weight:400;color:#222}
.work-item{position:absolute;left:11px;width:278px;height:74px;background:#e6e6e6;display:flex;align-items:center;gap:6px;padding:0 6px;font-size:10px;line-height:13px;letter-spacing:-.1px;color:#222}
.work-item.current{background:var(--navy);color:#fff}
.work-item.current::before{content:"";position:absolute;left:-9px;top:28px;border:9px solid transparent;border-left:0;border-right-color:var(--navy)}
.thumb{flex:0 0 70px;height:58px;background:linear-gradient(135deg,#6b5a4a,#c7b6a0)}
.pager{position:absolute;top:333px;width:19px;height:18px;background:#aaa}

.about h1{left:116px;top:552px;font-size:28px;font-weight:500;color:var(--navy)}
.about-copy{left:116px;top:602px;width:492px;font-size:14.5px;line-height:19px;color:#333}
.about-copy p{margin-bottom:18px}
.read-more{color:var(--green-dark);text-decoration:underline}

.search{left:629px;top:558px;width:245px;height:328px;background:var(--panel-blue);border-top:3px solid var(--green);padding:10px 20px;color:#fff}
.search label{display:block;font-size:14px;margin-bottom:4px}
.select{height:24px;background:#fff;color:#444;font-size:11px;line-height:24px;padding-left:12px;position:relative;margin-bottom:12px}
.select::after{content:"";position:absolute;right:9px;top:6px;width:7px;height:7px;border-right:2px solid #333;border-bottom:2px solid #333;transform:rotate(45deg)}
.pair{display:flex;gap:16px}.pair>div{flex:1}
.search-btn{height:26px;background:var(--green);text-align:center;font-size:14px;line-height:26px;margin-top:2px}

.services h2{left:116px;top:918px;font-size:23px;font-weight:500;color:var(--navy)}
.service-list{top:958px;list-style:none;font-size:14.5px;line-height:23.3px;color:#333}
.service-list li{padding-left:23px;position:relative}
.service-list li::before{content:"»";position:absolute;left:0;color:var(--green);font-weight:700}

.news{left:629px;top:920px;width:245px;height:214px;background:var(--card)}
.tabs{display:flex;height:39px}
.tab{flex:1;font-size:14px;line-height:39px;text-align:center;background:var(--green);color:#fff}
.tab.inactive{background:#fff;color:#222;border:1px solid var(--green)}
.news-item{display:flex;gap:8px;padding:12px 5px 0;font-size:11px;line-height:13px;color:#222}
.news-pic{flex:0 0 54px;height:57px}
.news-item a{display:block;margin-top:4px;color:var(--green-dark);text-decoration:underline;font-weight:500}

.site-footer{left:0;top:1164px;width:990px;height:36px;background:var(--navy);color:#fff;font-size:13px;line-height:36px;padding-left:116px}
.social{right:102px;top:8px;display:flex;gap:5px}
.social span{width:21px;height:21px;border-radius:50%;background:#fff}
</style>
</head>
<body>
<header class="site-header abs">
  <div class="brand abs"><span>TQ Sounds</span><span class="brand-mark"></span></div>
  <div class="phones abs">MEL&nbsp; +61 3 9000 4127<br>SYD&nbsp; +61 2 9000 8361</div>
  <nav class="main-nav abs">
    <a class="active" href="#">HOME</a><a href="#">RATES</a><a href="#">ABOUT US</a><a href="#">FAQS</a><a href="#">PAYMENTS</a><a href="#">LOGIN</a><a href="#">CONTACT</a>
  </nav>
</header>

<section class="feature-band abs">
</section>

<div class="video abs">
  <div class="video-frame abs" role="img" aria-label="Video still: guests with wine glasses chatting at a showcase event"></div>
  <div class="video-title abs">Lisette Aunger&nbsp; Crunchwell Bakes Sensations</div>
  <svg class="abs" style="left:604px;top:6px" width="16" height="16" viewBox="0 0 16 16"><g fill="#fff"><circle cx="12" cy="3" r="2.3"/><circle cx="4" cy="8" r="2.3"/><circle cx="12" cy="13" r="2.3"/></g><path d="M12 3 4 8l8 5" stroke="#fff" stroke-width="1.5" fill="none"/></svg>
  <div class="play abs"></div>
  <svg class="abs" style="left:306px;top:157px" width="20" height="22"><path d="M0 0 20 11 0 22z" fill="#fff"/></svg>
  <div class="controls abs">
    <svg class="abs" style="left:16px;top:12px" width="14" height="14"><path d="M0 0 14 7 0 14z" fill="#ccc"/></svg>
    <svg class="abs" style="left:58px;top:12px" width="20" height="14"><path d="M0 4h4l5-4v14l-5-4H0z" fill="#ccc"/><path d="M12 4l6 6M18 4l-6 6" stroke="#ccc" stroke-width="1.5"/></svg>
    <span class="abs" style="left:98px;top:11px"><b style="color:#fff">0:00</b> / 2:14</span>
    <svg class="abs" style="left:528px;top:13px" width="12" height="12"><circle cx="6" cy="6" r="6" fill="#bbb"/></svg>
    <svg class="abs" style="left:604px;top:10px" width="18" height="16" fill="none" stroke="#ccc" stroke-width="2"><path d="M1 5V1h5M12 1h5v4M17 11v4h-5M6 15H1v-4"/></svg>
  </div>
  <div class="progress abs"></div>
  <svg class="abs" style="left:-6px;top:333px" width="14" height="14"><circle cx="7" cy="7" r="6" fill="#ddd"/></svg>
</div>

<aside class="recent abs">
  <h2>RECENT WORK</h2>
  <div class="work-item" style="top:41px"><div class="thumb" role="img" aria-label="Voice artist at a studio microphone"></div><p>Lorem ipsum dolor sit amet, consectetur adipisicing elit, sed do eiusmod tempor incididunt ut labore et dolore magna</p></div>
  <div class="work-item current" style="top:137px"><div class="thumb" role="img" aria-label="Sound engineer at a mixing desk"></div><p>Lorem ipsum dolor sit amet, consectetur adipisicing elit, sed do eiusmod tempor incididunt ut labore et dolore magna</p></div>
  <div class="work-item" style="top:233px"><div class="thumb" role="img" aria-label="Recording session in a booth"></div><p>Lorem ipsum dolor sit amet, consectetur adipisicing elit, sed do eiusmod tempor incididunt ut labore et dolore magna</p></div>
  <div class="pager" style="left:11px"></div>
  <div class="pager" style="left:40px"></div>
  <svg class="abs" style="left:15px;top:338px" width="40" height="9" fill="none" stroke="#333" stroke-width="1.4"><path d="M1 8 6 2l5 6M30 1l5 6 5-6"/></svg>
</aside>

<section class="about">
  <h1 class="abs">ABOUT TQ SOUNDS</h1>
  <div class="about-copy abs">
    <p>TQ Sounds is one of Australia's most successful voice over artists' agencies. It has long been established as a friendly, professional and high quality Australian agency that has a singular focus on the business of voice overs. The company represents over 120 of Australia's most exceptional voice artists as well as high profile actors across a wide range of styles, ages, accents, characters and foreign languages.</p>
    <p>The management team of Owen Parridge, Ruth Kalvane and Dana Osterly supported by Managing Director Miles Harbrook and accounts manager Irena Volkat all live and breathe voice overs. They are not distracted by repping anyone other than talented, professional voice overs artists. TQ Sounds staff understand the field intimately and service hundreds of customers in a friendly and constructive manner every day.</p>
    <a class="read-more" href="#">Read More</a>
  </div>
</section>

<form class="search abs">
  <label>Serach By Name</label><div class="select">Please Select</div>
  <label>Location</label><div class="select">Select LOcation</div>
  <label>Voice Type</label><div class="select">Any</div>
  <div class="pair"><div><label>Language</label><div class="select">Any</div></div><div><label>Accent</label><div class="select">Any</div></div></div>
  <div class="pair"><div><label>Sex</label><div class="select">Any</div></div><div><label>Age</label><div class="select">Any</div></div></div>
  <div class="search-btn">Search</div>
</form>

<section class="services">
  <h2 class="abs">OUR SERVICES</h2>
  <ul class="service-list abs" style="left:116px">
    <li>Broadcast Advertising</li><li>TV and Radio Imaging</li><li>Promotions</li><li>IVR</li><li>Messages on Hold</li><li>Documentary narration</li><li>Website presentation</li>
  </ul>
  <ul class="service-list abs" style="left:336px">
    <li>Corporate</li><li>Multi-media</li><li>Animation</li><li>Computer Games</li><li>Character Voices</li><li>Foreign Language</li><li>Every conceivable voice type<br>and usage</li>
  </ul>
</section>

<aside class="news abs">
  <div class="tabs"><div class="tab">LATEST NEWS</div><div class="tab inactive">TQ SPOTLIGHT</div></div>
  <div class="news-item"><div class="news-pic" role="img" aria-label="Children's television series title card" style="background:linear-gradient(135deg,#1aa0b0,#7fd0c8)"></div><div>The new children's television series WILLA featuring Australian legends Nora Blayde<a href="#">Read More</a></div></div>
  <div class="news-item"><div class="news-pic" role="img" aria-label="Portrait of a featured voice artist" style="background:linear-gradient(135deg,#2b2b2b,#9a9a9a)"></div><div>The new children's television series WILLA featuring Australian legends Nora Blayde<a href="#">Read More</a></div></div>
</aside>

<footer class="site-footer abs">© 2015 Copyright TQ Sounds. All Rights Reserved.
  <div class="social abs"><span></span><span></span><span></span><span></span></div>
</footer>
</body>
</html>
```